Brochure/flyer for our trip to Paris

Our company is taking us all on a summer trip to Paris. We have some key information that we need to tell everybody about the trip. We think a nicely designed brochure or flyer, which uses our brand colours and guidelines, would be something nice to keep during the trip and as a memento afterwards.

We are looking for a brochure or a flyer which contains all the info in the attached document.

This needs to happen really fast as we actually go to Paris on the 13th August. We also need time to print it!

We can provide a library of icons. All images in the document can be changed. you don't have to use the images in the document.

Target Market(s)

People in our company. They are fun and as this is for a party the flyer needs to feel uplifting.

Industry/Entity Type

Health

Font styles to use
Other font styles liked:
• Nexa - please see attached font.

Requirements
Must have
• Designers must stick to our brand guideline, font and the colours we use.
• Please also see attached content for the flyer.
• This website shows our style - https://www.kelotrix.com/fr
Should not have
• Please don't make it too tacky or too much about French things. It can be a bit playful but not too much.

```html
<!DOCTYPE html>
<html lang="en">
<head>
<meta charset="utf-8">
<title>Kelotrix – A summer trip to Paris</title>
<link rel="stylesheet" href="https://fonts.googleapis.com/css2?family=Montserrat:wght@400;600;700&family=Dancing+Script:wght@600;700&display=swap">
<style>
  :root {
    --backdrop: #e6e6e6;
    --paper: #f6f4f4;
    --brand-blue: #4a7bbd;
    --brand-blue-light: #5d8dcc;
    --heading-navy: #2f3f86;
    --ink: #2a2a2a;
    --white: #ffffff;
    --map-green: #c3c62f;
    --accent-orange: #e8622a;
    --headline-blue: #4a86c8;
    --tower-blue: #4a78c0;
    --sky: #dfe8f5;
  }
  * { box-sizing: border-box; margin: 0; padding: 0; }
  html, body {
    width: 1200px; height: 1000px; overflow: hidden;
    background: var(--backdrop);
    font-family: "Montserrat", sans-serif;
  }
  .brochure {
    position: absolute; left: 60px; top: 120px;
    width: 1080px; height: 760px;
    background: var(--paper);
    overflow: hidden;
    box-shadow: 0 6px 24px rgba(0,0,0,0.12);
  }
  .brochure__wave { position: absolute; inset: 0; width: 1080px; height: 760px; }
  .brochure__fold {
    position: absolute; left: 539px; top: 0; width: 2px; height: 760px;
    background: rgba(0,0,0,0.05);
  }

  /* Inside left: visits */
  .visits__title {
    position: absolute; left: 50px; top: 40px;
    font-size: 19px; font-weight: 700; color: var(--heading-navy);
  }
  .visits__intro {
    position: absolute; left: 50px; top: 82px; width: 150px;
    font-size: 12.5px; line-height: 1.45; color: var(--ink);
  }
  .visits__map {
    position: absolute; left: 215px; top: 80px; width: 300px; height: 210px;
    border-radius: 40px 60px 50px 70px;
    background: radial-gradient(ellipse at 50% 50%, var(--map-green) 60%, #dcdc7a 100%);
  }

  /* Inside left: more information */
  .info {
    position: absolute; left: 50px; top: 420px; width: 480px;
    color: var(--white);
  }
  .info__title { font-size: 16px; font-weight: 600; margin-bottom: 14px; }
  .info__item { font-size: 11px; line-height: 1.5; margin-bottom: 7px; }
  .info__link { display: block; font-size: 10px; font-weight: 700; white-space: nowrap; }

  /* Front cover */
  .cover__tower {
    position: absolute; left: 575px; top: 175px; width: 110px; height: 330px;
    border-radius: 50px 50px 12px 12px;
    background: linear-gradient(180deg, var(--sky) 0%, var(--tower-blue) 45%, #3d4f9a 100%);
    opacity: 0.85;
  }
  .cover__balloons {
    position: absolute; left: 830px; top: 215px; width: 90px; height: 70px;
    border-radius: 35px;
    background: linear-gradient(135deg, #f3b79c 0%, var(--accent-orange) 100%);
    opacity: 0.6;
  }
  .cover__train {
    position: absolute; left: 985px; top: 420px; width: 95px; height: 80px;
    border-radius: 20px 0 0 20px;
    background: linear-gradient(90deg, var(--accent-orange) 0%, #f0916a 100%);
    opacity: 0.85;
  }
  .cover__headline {
    position: absolute; left: 680px; top: 285px; width: 300px;
    font-family: "Dancing Script", cursive;
    line-height: 1;
  }
  .cover__headline-greeting {
    display: block; margin-left: 28px;
    font-size: 64px; font-weight: 600; color: var(--headline-blue);
  }
  .cover__headline-city {
    display: block; margin-top: -6px;
    font-size: 132px; font-weight: 700; color: var(--accent-orange);
  }
  .cover__brand {
    position: absolute; right: 50px; bottom: 70px;
    font-size: 46px; font-weight: 600; color: var(--white); text-align: right;
    line-height: 1;
  }
  .cover__tagline {
    position: absolute; right: 50px; bottom: 40px;
    font-size: 16px; font-weight: 400; color: var(--white);
  }
</style>
</head>
<body>
  <main class="brochure">
    <svg class="brochure__wave" viewBox="0 0 1080 760" aria-hidden="true">
      <path d="M0,285 C250,265 420,320 540,385 C700,470 880,610 1080,545 L1080,760 L0,760 Z" fill="var(--brand-blue-light)"/>
      <path d="M0,310 C250,295 420,350 540,420 C700,505 880,640 1080,575 L1080,760 L0,760 Z" fill="var(--brand-blue)"/>
    </svg>
    <div class="brochure__fold"></div>

    <section class="visits">
      <h2 class="visits__title">Book your visits in Paris :</h2>
      <p class="visits__intro">If you'd like to see some of the most famous monuments in Paris, we recommend you book your tickets in advance. Here are the most touristic places in Paris :</p>
      <div class="visits__map" role="img" aria-label="Illustrated map of Paris with its districts, river and main landmarks"></div>
    </section>

    <section class="info">
      <h3 class="info__title">More Information :</h3>
      <p class="info__item">Book tickets online for "La Tour eiffel" (Tube 9 and 6, "Trocadero" station)
        <span class="info__link">http://www.irontowervisits.com/en/planyourvisit/buytickets.html</span></p>
      <p class="info__item">Sacré coeur : free entrance (Tube 2 and 12)
        <span class="info__link">http://www.hilltopbasilica.org/english/visitand-audioguide/article/openinghours</span></p>
      <p class="info__item">Le Louvre : we advise you to visit the place from outside only, time is too short for the museum
        <span class="info__link">http://www.grandgalleryparis.com/en/visitortips</span></p>
      <p class="info__item">Notre Dame : Walking distance from the hotel or line 4 ("Cité" station)
        <span class="info__link">http://www.islecathedral.org/spip.php?article314</span></p>
      <p class="info__item">Musée d'Orsay : Buy ticket online line 12
        <span class="info__link">http://www.riversidestationmuseum.com/en/visit/admission/ticketpurchase.html</span></p>
    </section>

    <section class="cover">
      <div class="cover__tower" role="img" aria-label="Illustration of the Eiffel Tower rising out of clouds"></div>
      <div class="cover__balloons" role="img" aria-label="Illustration of two striped hot-air balloons"></div>
      <div class="cover__train" role="img" aria-label="Illustration of an orange train on a track"></div>
      <h1 class="cover__headline">
        <span class="cover__headline-greeting">Bonjour</span>
        <span class="cover__headline-city">Paris</span>
      </h1>
      <p class="cover__brand">Kelotrix</p>
      <p class="cover__tagline">A summer trip to Paris</p>
    </section>
  </main>
</body>
</html>
```